Home & Landing Page REDESIGN needed for Psychology Group

We need a redesign for the template home and landing pages for our psychology group.

Ideally we want a similar layout in the core features, but we want a newer, fresher and more professional design overall.

Our developer will implement the changes from the winning design.

Logo to stay the same.

Please ensure you stay within the same color scheme as the LOGOs 3 main colors.

We want to convey professional, modern, friendly and caring.

Here is the main page template:

http://www.lowrenclinic.com.au/psychologist-melbourne/

and

http://www.lowrenclinic.com.au

*note: we are creating an intro video, please ensure it is included in your brief, near the top of the site* - it is not included on the current site yet but we need it included in all designs.

Target Market(s)

people suffering anxiety, depression or stress that need a psychologist

Industry/Entity Type

Psychology

Number of Pages Required

2 page

Font styles to use
Sans Serif

Colors
86cfc6
85cae6
b7a5cd

Requirements
Must have
• search bar functionality in the top fold of the page, strong focus that we are experienced in anxiety, depression and stress counselling.
• Lots of images and pictures.
• **MUST HAVE: the search square area as it is, unfortunately this cannot be a bar due to development issues with the theme. Please make sure all designs have the search function like it is showing (in a square/rectangle)**
• Must also keep:
• - content area for both home page and city landing pages
• - banner area with search bar same style
• - an area for faqs and blog
• - locations across Australia
• We want most of the same areas, just a refresh so they look better and more polished and professional.
• We are also having an intro video designed, so please include that in your design. (its not in our current web design, but needs to be in the new design)
Should not have
• No orange type colors

```html
<!DOCTYPE html>
<html lang="en">
<head>
<meta charset="utf-8">
<title>Lowren Clinic – Psychologists</title>
<link href="https://fonts.googleapis.com/css2?family=Roboto:wght@300;400;500;700&display=swap" rel="stylesheet">
<style>
:root{
  --purple:#5d58a6;
  --purple-band:#6c69b4;
  --sky:#5dc0df;
  --sky-light:#8fd0ea;
  --teal:#86cfc6;
  --lilac:#b7a5cd;
  --ink:#444;
  --muted:#666;
  --card:#f1f1f1;
  --footer:#ececec;
  --white:#fff;
}
*{box-sizing:border-box;margin:0;padding:0}
html,body{width:1200px;height:2857px;overflow:hidden}
body{font-family:'Roboto',Arial,sans-serif;color:var(--ink);background:var(--white);position:relative}
a{color:inherit;text-decoration:none}

/* header */
.site-header{height:118px;border:1px solid #ddd;position:relative;background:var(--white)}
.brand{position:absolute;left:88px;top:30px;display:flex;align-items:center;gap:12px}
.brand-dot{width:44px;height:44px;border-radius:50%;background:var(--teal)}
.brand-name{font-size:26px;font-weight:500;color:var(--purple);line-height:1}
.header-btn{position:absolute;top:38px;height:42px;border:2px solid var(--teal);color:var(--teal);font-size:13px;display:flex;align-items:center;justify-content:center;gap:10px;letter-spacing:.3px}
.btn-appoint{left:802px;width:177px}
.btn-sign{left:998px;width:115px}

/* nav */
.main-nav{height:55px;background:var(--sky);display:flex;align-items:center;padding-left:88px}
.main-nav a{color:var(--white);font-size:14px;font-weight:500;margin-right:48px;display:flex;align-items:center;gap:8px}
.main-nav a.active{color:var(--purple)}
.main-nav .caret{width:0;height:0;border-left:4px solid transparent;border-right:4px solid transparent;border-top:5px solid var(--white)}

/* hero */
.hero{position:relative;height:553px;overflow:hidden}
.hero-photo{position:absolute;inset:0;background:linear-gradient(100deg,#d8dde2 0%,#c9c3bd 35%,#d7b59a 62%,#9c8a7d 100%)}
.video-play{position:absolute;left:540px;top:233px;width:120px;text-align:center;color:var(--white);font-size:12px;font-weight:500;white-space:nowrap}
.video-play svg{display:block;margin:0 auto 10px}
.search-box{position:absolute;left:0;right:0;top:417px;height:136px;background:rgba(60,60,70,.55);border-top:1px solid rgba(255,255,255,.7)}
.search-field{position:absolute;top:50px;height:42px;background:var(--white);display:flex;align-items:center;font-size:13px;color:var(--muted);padding-left:12px}
.search-field .drop{position:absolute;right:0;top:0;width:32px;height:42px;background:var(--purple);display:flex;align-items:center;justify-content:center}
.search-label{position:absolute;top:22px;color:var(--white);font-size:13px}
.radius{position:absolute;left:790px;top:42px;color:var(--white);font-size:12px}
.radius-track{position:absolute;left:790px;top:70px;width:183px;height:5px;background:var(--white);border-radius:3px}
.radius-knob{position:absolute;left:63px;top:-5px;width:15px;height:15px;border-radius:50%;background:var(--sky);border:2px solid var(--white)}
.search-btn{position:absolute;left:1000px;top:50px;width:102px;height:38px;background:var(--purple);color:var(--white);font-size:13px;display:flex;align-items:center;justify-content:center;border-radius:3px}
.slide-arrows{position:absolute;left:576px;top:530px;width:48px;height:30px;border-radius:50%;background:var(--white);display:flex;align-items:center;justify-content:center;gap:6px;color:var(--ink);font-size:14px}

/* welcome */
.welcome{height:583px;text-align:center;position:relative}
.section-title{font-size:25px;color:var(--purple);font-weight:500;letter-spacing:.3px}
.welcome .section-title{padding-top:76px}
.welcome-lead{width:540px;margin:14px auto 0;font-size:14px;line-height:24px;color:var(--muted)}
.service-cards{position:absolute;left:88px;top:192px;display:flex;gap:38px}
.service-card{width:316px;height:311px;background:var(--card);padding-top:34px}
.service-icon{width:92px;height:92px;border-radius:50%;background:var(--sky-light);margin:0 auto;display:flex;align-items:center;justify-content:center}
.service-card h3{font-size:16px;font-weight:500;color:var(--purple);margin-top:22px}
.service-card p{font-size:13px;line-height:20px;color:var(--muted);padding:6px 34px 0;text-align:justify;text-align-last:center}
.service-card p b{color:var(--purple)}
.quiz-btn{display:inline-block;margin-top:16px;border:1.5px solid var(--purple);color:var(--purple);font-size:12px;padding:8px 14px;border-radius:4px}

/* faq */
.faq-band{height:411px;background:var(--sky-light);position:relative}
.faq-photo{position:absolute;left:88px;top:49px;width:497px;height:311px;border:5px solid var(--white);background:linear-gradient(120deg,#f2ede6 0%,#e6e1d8 45%,#8c8a88 70%,#c8c4bf 100%)}
.faq-panel{position:absolute;left:615px;top:49px;width:498px;height:311px;background:#eef2f0;box-shadow:0 2px 6px rgba(0,0,0,.15);padding:40px 50px}
.faq-panel h2{font-size:19px;font-weight:400;color:var(--purple);padding-bottom:14px;border-bottom:2px solid var(--purple);display:inline-block;white-space:nowrap}
.faq-list{list-style:none;margin-top:20px}
.faq-list li{font-size:13px;color:var(--ink);margin-bottom:12px;display:flex;gap:12px}
.faq-list li::before{content:"⟶";color:var(--purple)}
.faq-list li.open a{text-decoration:underline}
.faq-list .excerpt{display:block;color:var(--teal);font-size:12px;line-height:17px;margin-top:4px}

/* blogs */
.blogs{height:349px;position:relative}
.blogs .section-title{position:absolute;left:88px;top:68px}
.blogs .title-rule{position:absolute;left:88px;top:108px;width:50px;height:2px;background:var(--purple)}
.blog-item{position:absolute;top:140px;display:flex;gap:20px}
.blog-thumb{width:136px;height:136px;border-radius:50%;border:5px solid #ddd;background:radial-gradient(circle at 50% 40%,#d9c8b8,#a9b8c6);flex:none}
.blog-item h4{font-size:14px;font-weight:500;color:#333;margin-top:18px;white-space:nowrap}
.blog-item p{font-size:13px;line-height:19px;color:var(--muted);margin-top:6px;text-align:justify}
.read-more{font-size:12px;color:var(--purple);font-weight:500;margin-top:2px;display:block}
.blog-nav{position:absolute;left:1012px;top:253px;display:flex;gap:16px}
.blog-nav span{width:30px;height:26px;border:1px solid #bbb;display:flex;align-items:center;justify-content:center;font-size:12px}

/* locations */
.locations{height:413px;background:var(--purple-band);position:relative;color:var(--white)}
.locations .section-title{color:var(--white);text-align:center;padding-top:64px}
.loc-arrow{position:absolute;top:208px}
.loc-card{position:absolute;top:154px;width:204px;height:187px;border:1px solid rgba(255,255,255,.8)}
.loc-pin{position:absolute;left:78px;top:-25px;width:48px;height:48px;border-radius:50%;background:var(--white);display:flex;align-items:center;justify-content:center}
.loc-card h3{text-align:center;font-size:15px;font-weight:400;margin-top:36px}
.loc-card ul{list-style:none;padding-left:52px;margin-top:4px}
.loc-card li{font-size:12px;line-height:22px}
.loc-card li::before{content:"›";margin-right:14px}

/* footer */
.site-footer{height:375px;background:var(--footer);position:relative}
.footer-col{position:absolute;top:56px}
.footer-col h4{font-size:19px;font-weight:500;color:#333;margin-bottom:22px}
.contact-row{display:flex;gap:16px;margin-bottom:18px}
.contact-icon{width:38px;height:38px;border-radius:50%;border:1.5px solid var(--purple);display:flex;align-items:center;justify-content:center;flex:none}
.contact-row b{display:block;font-size:13px;color:var(--purple);font-weight:500}
.contact-row span{font-size:13px;color:var(--muted)}
.cat-list,.follow-list{list-style:none}
.cat-list li{font-size:12px;color:var(--muted);line-height:25px}
.cat-list li::before{content:"›";margin-right:14px}
.follow-list li{font-size:13px;color:var(--muted);line-height:27px;display:flex;align-items:center;gap:12px}
.follow-list li::before{content:"";width:13px;height:13px;background:var(--purple);border-radius:2px}
.news-note{font-size:12px;color:var(--muted)}
.news-input{margin-top:14px;width:308px;height:38px;border:1px solid #ccc;border-radius:4px;background:var(--white);font-size:12px;font-style:italic;color:#999;display:flex;align-items:center;padding-left:14px}
.subscribe{display:inline-block;margin-top:16px;background:var(--purple);color:var(--white);font-size:13px;font-weight:500;padding:11px 14px;border-radius:3px}
.footer-rule{position:absolute;left:88px;right:88px;top:305px;height:1px;background:#ccc}
.copyright{position:absolute;left:0;right:0;top:328px;text-align:center;font-size:12px;color:var(--muted)}
</style>
</head>
<body>

<header class="site-header">
  <div class="brand">
    <span class="brand-dot"></span>
    <div class="brand-name">Lowren Clinic</div>
  </div>
  <a class="header-btn btn-appoint" href="#">MAKE AN APPOINTMENT</a>
  <a class="header-btn btn-sign" href="#">
    <svg width="14" height="14" viewBox="0 0 14 14"><circle cx="7" cy="4" r="3.2" fill="#86cfc6"/><path d="M1 14c0-4 2.7-6 6-6s6 2 6 6z" fill="#86cfc6"/></svg>SIGN IN</a>
</header>

<nav class="main-nav">
  <a class="active" href="#">HOME</a>
  <a href="#">COUNSELLING TYPES <span class="caret"></span></a>
  <a href="#">PSYCHOLOGIST LOCATIONS <span class="caret"></span></a>
  <a href="#">FAQS</a>
  <a href="#">FEES &amp; REBATES</a>
  <a href="#">QUIZZES <span class="caret"></span></a>
  <a href="#">CONTACT</a>
</nav>

<section class="hero">
  <div class="hero-photo" role="img" aria-label="Photo of a smiling psychologist holding a clipboard"></div>
  <a class="video-play" href="#">
    <svg width="38" height="38" viewBox="0 0 38 38"><circle cx="19" cy="19" r="17" fill="none" stroke="#fff" stroke-width="3"/><path d="M15 11l12 8-12 8z" fill="#fff"/></svg>
    WATCH VIDEO
  </a>
  <form class="search-box">
    <span class="search-label" style="left:98px">Search For :</span>
    <span class="search-label" style="left:326px">Search near :</span>
    <div class="search-field" style="left:98px;width:216px">Type of Counselling<span class="drop"><svg width="10" height="6"><path d="M0 0h10L5 6z" fill="#fff"/></svg></span></div>
    <div class="search-field" style="left:326px;width:216px">City -<span class="drop"><svg width="10" height="6"><path d="M0 0h10L5 6z" fill="#fff"/></svg></span></div>
    <div class="search-field" style="left:554px;width:216px">Enter Your Suburb<span class="drop"><svg width="10" height="6"><path d="M0 0h10L5 6z" fill="#fff"/></svg></span></div>
    <span class="radius">Search in radius 50 kilometers</span>
    <div class="radius-track"><span class="radius-knob"></span></div>
    <span class="search-btn">SEARCH</span>
  </form>
  <span class="slide-arrows">‹ ›</span>
</section>

<section class="welcome">
  <h1 class="section-title">WELCOME TO LOWREN CLINIC</h1>
  <p class="welcome-lead">We are psychologists passionate about helping you overcome your depression, anxiety and stress and create a life you love.</p>
  <div class="service-cards">
    <article class="service-card">
      <div class="service-icon"><svg width="40" height="40" viewBox="0 0 40 40"><circle cx="20" cy="20" r="17" fill="none" stroke="#fff" stroke-width="2.5"/><circle cx="14" cy="16" r="2" fill="#fff"/><circle cx="26" cy="16" r="2" fill="#fff"/><path d="M12 24q8 7 16 0" fill="none" stroke="#fff" stroke-width="2.5"/></svg></div>
      <h3>DEPRESSION COUNSELLING</h3>
      <p>Are you feeling empty, hopeless and despairing? Do you have huge ups and do you have Male <b>&gt;&gt;</b></p>
      <a class="quiz-btn" href="#">QUIZ NOW</a>
    </article>
    <article class="service-card">
      <div class="service-icon"><svg width="42" height="40" viewBox="0 0 42 40"><circle cx="16" cy="22" r="9" fill="none" stroke="#fff" stroke-width="5" stroke-dasharray="4 3"/><circle cx="16" cy="22" r="3" fill="#fff"/><circle cx="31" cy="11" r="6" fill="none" stroke="#fff" stroke-width="4" stroke-dasharray="3 2.5"/></svg></div>
      <h3>ANXIETY COUNSELLING</h3>
      <p>Do you feel tense, edgy and wound up? Do you worry a lot, or think in worry obsessive ways? <b>&gt;&gt;</b></p>
      <a class="quiz-btn" href="#">QUIZ NOW</a>
    </article>
    <article class="service-card">
      <div class="service-icon"><svg width="40" height="40" viewBox="0 0 40 40"><path d="M8 36V24C4 20 4 8 16 5c10-2 18 4 17 13l3 6h-4v6c0 3-2 4-5 4h-3v2z" fill="#fff"/><circle cx="19" cy="17" r="5" fill="#8fd0ea"/></svg></div>
      <h3>STRESS COUNSELLING</h3>
      <p>Do you feel tired but also still wired up? Do you many struggle with too many expectations? <b>&gt;&gt;</b></p>
      <a class="quiz-btn" href="#">QUIZ NOW</a>
    </article>
  </div>
</section>

<section class="faq-band">
  <div class="faq-photo" role="img" aria-label="Photo of a man talking with a psychologist in a bright office"></div>
  <div class="faq-panel">
    <h2>FREQUENTLY ASKED QUESTIONS</h2>
    <ul class="faq-list">
      <li class="open"><span><a href="#">Exciting news in Treating Anxiety and Depression</a><span class="excerpt">In recent years there has been a huge amount of research in neuroscience within the brain these ways..</span></span></li>
      <li>Why come to us for help with your Anxiety and Depression?</li>
      <li>Costs of counselling sessions</li>
      <li>What rebates are available?</li>
      <li>What treatment Modalities do we use as Psychologists?</li>
    </ul>
  </div>
</section>

<section class="blogs">
  <h2 class="section-title">LATEST BLOGS</h2>
  <span class="title-rule"></span>
  <article class="blog-item" style="left:88px;width:436px">
    <div class="blog-thumb" role="img" aria-label="Photo of a worried older woman"></div>
    <div>
      <h4>DO YOU HAVE AGORAPHOBIA?</h4>
      <p>Do you struggle to leave the house without a friend? Are you frightened of what might happen if you...</p>
      <a class="read-more" href="#">READ MORE &gt;&gt;</a>
    </div>
  </article>
  <article class="blog-item" style="left:615px;width:480px">
    <div class="blog-thumb" role="img" aria-label="Photo of a thoughtful woman"></div>
    <div>
      <h4>WHAT IS A GENERALISED ANXIETY DISORDER?</h4>
      <p>You're worried..... Constantly and without relief, your mind just can't stop contemplating the 'what if's?' What if...</p>
      <a class="read-more" href="#">READ MORE &gt;&gt;</a>
    </div>
  </article>
  <div class="blog-nav"><span>‹</span><span>›</span></div>
</section>

<section class="locations">
  <h2 class="section-title">OUR LOCATIONS ACROSS AUSTRALIA</h2>
  <svg class="loc-arrow" style="left:184px" width="22" height="36"><path d="M18 2L4 18l14 16" fill="none" stroke="#fff" stroke-width="3"/></svg>
  <svg class="loc-arrow" style="left:996px" width="22" height="36"><path d="M4 2l14 16L4 34" fill="none" stroke="#fff" stroke-width="3"/></svg>
  <div class="loc-card" style="left:267px">
    <span class="loc-pin"><svg width="14" height="20" viewBox="0 0 14 20"><path d="M7 0a7 7 0 017 7c0 5-7 13-7 13S0 12 0 7a7 7 0 017-7z" fill="#6c69b4"/><circle cx="7" cy="7" r="2.5" fill="#fff"/></svg></span>
    <h3>BRISBANE</h3>
    <ul><li>Brisbane CBD</li><li>Carindale</li><li>Ashgrove</li><li>Indooroopilly</li><li>Parkinson</li></ul>
  </div>
  <div class="loc-card" style="left:497px">
    <span class="loc-pin"><svg width="14" height="20" viewBox="0 0 14 20"><path d="M7 0a7 7 0 017 7c0 5-7 13-7 13S0 12 0 7a7 7 0 017-7z" fill="#6c69b4"/><circle cx="7" cy="7" r="2.5" fill="#fff"/></svg></span>
    <h3>SYDNEY</h3>
    <ul><li>Sydney CBD</li><li>Mosman</li><li>Green Square</li><li>Windsor</li></ul>
  </div>
  <div class="loc-card" style="left:730px">
    <span class="loc-pin"><svg width="14" height="20" viewBox="0 0 14 20"><path d="M7 0a7 7 0 017 7c0 5-7 13-7 13S0 12 0 7a7 7 0 017-7z" fill="#6c69b4"/><circle cx="7" cy="7" r="2.5" fill="#fff"/></svg></span>
    <h3>PERTH</h3>
    <ul><li>Perth CBD</li><li>Midland</li><li>Nedlands</li><li>West Leederville</li></ul>
  </div>
</section>

<footer class="site-footer">
  <div class="footer-col" style="left:88px">
    <h4>GET IN TOUCH</h4>
    <div class="contact-row"><span class="contact-icon"><svg width="12" height="16" viewBox="0 0 14 20"><path d="M7 0a7 7 0 017 7c0 5-7 13-7 13S0 12 0 7a7 7 0 017-7z" fill="#5d58a6"/><circle cx="7" cy="7" r="2.5" fill="#fff"/></svg></span><div><b>AUSTRALIA</b><span>12 Example Lane</span></div></div>
    <div class="contact-row"><span class="contact-icon"><svg width="16" height="16" viewBox="0 0 16 16"><path d="M3 1l3 3-2 2c1 2 3 4 5 5l2-2 3 3-2 3C7 15 1 9 1 3z" fill="#5d58a6"/></svg></span><div><b>CALL US</b><span>1300 555 014</span></div></div>
    <div class="contact-row"><span class="contact-icon"><svg width="16" height="12" viewBox="0 0 16 12"><rect width="16" height="12" rx="1" fill="#5d58a6"/><path d="M1 1l7 6 7-6" fill="none" stroke="#fff" stroke-width="1.5"/></svg></span><div><b>MAIL US</b><span>info@lowrenclinic.com.au</span></div></div>
  </div>
  <div class="footer-col" style="left:358px">
    <h4>CATEGORIES</h4>
    <ul class="cat-list"><li>Anxiety (6)</li><li>Counselling (3)</li><li>Depression (4)</li><li>Personal growth (3)</li><li>Psychological well being (10)</li><li>Self esteem (1)</li><li>Stress (2)</li></ul>
  </div>
  <div class="footer-col" style="left:624px">
    <h4>FOLLOW US</h4>
    <ul class="follow-list"><li>Community</li><li>Updates</li><li>Videos</li><li>Network</li><li>Gallery</li></ul>
  </div>
  <div class="footer-col" style="left:803px">
    <h4>NEWSLETTER</h4>
    <p class="news-note">Sign up for newsletters, events and the promotions</p>
    <div class="news-input">E mail Address..</div>
    <a class="subscribe" href="#">SUBSCRIBE</a>
  </div>
  <div class="footer-rule"></div>
  <p class="copyright">@copyright 2016 Lowren Clinic All Rights Reserved</p>
</footer>

</body>
</html>
```